Marnie Holloway 2014 Calendar

We need a 12 month, wall hanging Calendar design featuring the actress Marnie Holloway. It is a product for her fans and the feel of this years photographs is very otherworldly with saturated colors and the incorporation of elements such as fire, ice and water. We are looking for bold, graphic designs to support and reflect this feel. There is a very tight schedule for the completion of this calendar as it needs to go into production asap so any designers submitting concepts should have the ability and enthusiasm to dedicate the necessary time required to get this product to the printers quickly.
We have included three of the twelve photographs for you to use with a combination of vertical and horizontal images. Once the design is selected we will provide the remaining nine photos to be incorporated. These images are to be kept completely confidential please.
Thank you and we are looking forward to seeing your ideas!!
Industry/Entity Type
Product
Requirements
Must have
- Bio about Marnie Holloway, crédits for art director, photographer etc. Some negative space on cover so that it maybe autographed by actress. 12 months reflected in page design.

```html
<!DOCTYPE html>
<html lang="en">
<head>
<meta charset="utf-8">
<title>Marnie Holloway Calendar – August 2014</title>
<link rel="stylesheet" href="https://fonts.googleapis.com/css2?family=Exo+2:wght@500&family=Signika:wght@400;600&display=swap">
<style>
  :root {
    --ember-dark: #1a0c06;
    --ember-mid: #5a2a10;
    --ember-glow: #c8701f;
    --ember-bright: #f2a546;
    --band-veil: rgba(255, 255, 255, 0.62);
    --title-white: #eeeaea;
    --month-copper: #b06a1c;
    --weekday-copper: #b8752c;
    --cell-gold: rgba(186, 145, 58, 0.88);
    --cell-text: #fbf6ec;
    --bio-heading: #7a461a;
    --bio-body: #8a4a16;
  }
  html, body {
    margin: 0;
    padding: 0;
    overflow: hidden;
    background: #ffffff;
  }
  .calendar-page {
    position: relative;
    width: 849px;
    height: 1200px;
    overflow: hidden;
    font-family: "Signika", Arial, sans-serif;
  }
  .hero-photo {
    position: absolute;
    inset: 0;
    background:
      radial-gradient(ellipse 38% 30% at 52% 30%, rgba(200, 130, 70, 0.85), transparent 70%),
      radial-gradient(ellipse 30% 22% at 10% 45%, rgba(242, 165, 70, 0.55), transparent 70%),
      radial-gradient(ellipse 30% 22% at 88% 40%, rgba(242, 165, 70, 0.45), transparent 70%),
      radial-gradient(ellipse 40% 20% at 50% 98%, rgba(230, 120, 40, 0.7), transparent 70%),
      linear-gradient(180deg, var(--ember-dark) 0%, var(--ember-mid) 35%, #7a3a14 60%, var(--ember-mid) 85%, var(--ember-dark) 100%);
  }
  .portrait-name {
    position: absolute;
    left: 24px;
    top: 14px;
    margin: 0;
    font-family: "Exo 2", Arial, sans-serif;
    font-weight: 500;
    font-size: 46px;
    letter-spacing: 0.5px;
    color: var(--title-white);
  }
  .month-band {
    position: absolute;
    left: 0;
    top: 677px;
    width: 849px;
    height: 438px;
    background: var(--band-veil);
  }
  .month-title {
    position: absolute;
    left: 28px;
    top: 690px;
    margin: 0;
    font-weight: 600;
    font-size: 44px;
    letter-spacing: 1px;
    color: var(--month-copper);
    line-height: 1;
  }
  .weekday-row,
  .day-grid {
    position: absolute;
    left: 26px;
    display: grid;
    grid-template-columns: repeat(7, 56px);
    column-gap: 6px;
  }
  .weekday-row {
    top: 756px;
    font-weight: 600;
    font-size: 25px;
    color: var(--weekday-copper);
    text-align: center;
    line-height: 30px;
  }
  .day-grid {
    top: 792px;
    grid-auto-rows: 56px;
    row-gap: 6px;
  }
  .day-cell {
    background: var(--cell-gold);
    color: var(--cell-text);
    font-size: 28px;
    display: flex;
    align-items: center;
    justify-content: center;
  }
  .bio {
    position: absolute;
    left: 492px;
    top: 788px;
    width: 330px;
  }
  .bio-heading {
    margin: 0 0 10px;
    font-weight: 600;
    font-size: 24px;
    color: var(--bio-heading);
  }
  .bio-text {
    margin: 0;
    font-weight: 600;
    font-size: 19px;
    line-height: 21.5px;
    color: var(--bio-body);
  }
</style>
</head>
<body>
<main class="calendar-page">
  <div class="hero-photo" role="img" aria-label="Full-page photograph of the actress posing with hands in her hair, wearing chains and jewellery, surrounded by fiery sparks"></div>

  <h1 class="portrait-name">Marnie Holloway</h1>

  <section class="month-band" aria-label="August 2014"></section>
  <h2 class="month-title">AUGUST 2014</h2>

  <div class="weekday-row">
    <span>Mon</span><span>Tue</span><span>Wed</span><span>Thu</span><span>Fri</span><span>Sat</span><span>Sun</span>
  </div>

  <div class="day-grid">
    <span class="day-cell">28</span><span class="day-cell">29</span><span class="day-cell">30</span><span class="day-cell">31</span><span class="day-cell">1</span><span class="day-cell">2</span><span class="day-cell">3</span>
    <span class="day-cell">4</span><span class="day-cell">5</span><span class="day-cell">6</span><span class="day-cell">7</span><span class="day-cell">8</span><span class="day-cell">9</span><span class="day-cell">10</span>
    <span class="day-cell">11</span><span class="day-cell">12</span><span class="day-cell">13</span><span class="day-cell">14</span><span class="day-cell">15</span><span class="day-cell">16</span><span class="day-cell">17</span>
    <span class="day-cell">18</span><span class="day-cell">19</span><span class="day-cell">20</span><span class="day-cell">21</span><span class="day-cell">22</span><span class="day-cell">23</span><span class="day-cell">24</span>
    <span class="day-cell">25</span><span class="day-cell">26</span><span class="day-cell">27</span><span class="day-cell">28</span><span class="day-cell">29</span><span class="day-cell">30</span><span class="day-cell">1</span>
  </div>

  <aside class="bio">
    <h3 class="bio-heading">Some text about Marnie</h3>
    <p class="bio-text">Lorem ipsum dolor sit amet,<br>cu sea minim albucius, fugit<br>maluisset et mea.<br>Omnium propriae ad has, latine<br>eligendi iudicabit nam no.</p>
  </aside>
</main>
</body>
</html>
```